Label Redesign For Hemp Oil Tincture Bottle*

I need a label redesigned for Marbleleaf Hemp, current bottle label and logo is attached. The current label doesn't standout, not sure if its the font size or colors on the existing label. It is very important to have on the label that this is a Premium Full Spectrum Hemp Oil that is 2000mg. Then after the label is redesigned and approved, I would need to packaging to be designed to match the approved label design.
This Hemp oil has a relaxing effect to help ease mental and emotional stress, tension and worry. The Omega Fatty Acids it contains also naturally improves your mood and overall brain function, causing you to feel more alert and focused. Hemp Oil helps with insomnia. Take some 2-3 hours before bedtime, you will feel relaxed yet aware of how tired you are that it will lead to a good night's sleep. Hemp Oil helps ease chronic pain and inflammation from conditions such as arthritis, fibromyalgia, lupus, and MS. As a pain relief supplement, it is a safer, natural, non-chemical and non-addictive alternative to prescription painkillers.

Target Market(s)

Adults

Industry/Entity Type

Supplement

Font styles to use
Serif
Sans Serif

Colors

Designer to choose colors to be used in the design.

Requirements
Must have
• All information thats on current label but where it says 750 in the front of the existing label, it needs to say 2000. The 2000 should be prominent on the label.

```html
<!DOCTYPE html>
<html lang="en">
<head>
<meta charset="utf-8">
<title>Marbleleaf Hemp – Packaging and Label</title>
<link href="https://fonts.googleapis.com/css2?family=PT+Sans:wght@400;700&display=swap" rel="stylesheet">
<style>
  :root {
    --backdrop: #a9cba6;
    --green-dark: #2c7337;
    --green-mid: #3b8747;
    --green-accent: #2f9a3c;
    --white: #ffffff;
    --grey-mark: #8c8c8c;
  }
  * { box-sizing: border-box; margin: 0; padding: 0; }
  html, body { width: 1200px; height: 900px; overflow: hidden; }
  body {
    background: var(--backdrop);
    font-family: "PT Sans", Arial, sans-serif;
    color: var(--white);
    position: relative;
  }
  .carton { position: absolute; left: 170px; top: 150px; display: flex; }
  .carton-side {
    width: 130px; height: 600px;
    background: linear-gradient(180deg, var(--green-dark), #266530);
    display: flex; flex-direction: column;
  }
  .side-mark { height: 120px; margin: 12px 12px 0; background: var(--white); display: flex; align-items: center; justify-content: center; }
  .side-copy { font-size: 8px; line-height: 1.45; padding: 14px 10px; opacity: .9; }
  .side-band { background: var(--white); color: var(--green-accent); padding: 8px 10px; font-weight: 700; }
  .side-band .s1 { font-size: 15px; }
  .side-band .s2 { font-size: 11px; }
  .side-band .s3 { font-size: 10px; margin-top: 10px; color: var(--green-dark); }
  .side-foot { margin-top: auto; background: var(--white); color: var(--green-dark); font-size: 10px; font-weight: 700; text-align: center; padding: 10px 0; }
  .carton-front {
    width: 300px; height: 600px;
    background: linear-gradient(180deg, var(--green-mid), var(--green-dark));
    display: flex; flex-direction: column; align-items: center;
  }
  .brand-tile {
    width: 180px; height: 110px; background: var(--white);
    display: flex; align-items: center; justify-content: center; gap: 8px;
    color: var(--green-dark); font-weight: 700; font-size: 17px;
  }
  .brand-tile .dot { width: 12px; height: 12px; background: var(--green-accent); }
  .title { font-weight: 700; text-align: center; line-height: 1.05; margin: 26px 0 22px; }
  .carton-front .title { font-size: 46px; }
  .strength-band { width: 100%; background: var(--white); text-align: center; font-weight: 700; color: var(--green-accent); }
  .carton-front .strength-band { padding: 12px 0 14px; }
  .carton-front .p1 { font-size: 22px; }
  .carton-front .p2 { font-size: 16px; }
  .carton-front .p3 { font-size: 15px; margin-top: 8px; color: var(--green-dark); }
  .leaf-icon { border-radius: 50%; background: rgba(255,255,255,.75); }
  .carton-front .leaf-icon { width: 46px; height: 46px; margin: 34px 0 0; }
  .claims { text-align: center; font-weight: 700; margin-top: auto; }
  .carton-front .claims { padding-bottom: 22px; }
  .carton-front .c1 { font-size: 22px; margin-bottom: 8px; }
  .carton-front .c2, .carton-front .c3 { font-size: 17px; }
  .volume-band { width: 100%; background: var(--white); color: var(--green-dark); text-align: center; font-weight: 700; }
  .carton-front .volume-band { font-size: 18px; padding: 12px 0; }

  .bottle-label {
    position: absolute; left: 700px; top: 250px; width: 330px; height: 420px;
    background: linear-gradient(180deg, var(--green-mid), var(--green-dark));
    display: flex; flex-direction: column; align-items: center; padding-top: 16px;
  }
  .bottle-label .brand-tile { width: 140px; height: 72px; font-size: 14px; }
  .bottle-label .brand-tile .dot { width: 10px; height: 10px; }
  .bottle-label .title { font-size: 34px; margin: 16px 0 14px; }
  .bottle-label .strength-band { padding: 8px 0 10px; }
  .bottle-label .p1 { font-size: 18px; }
  .bottle-label .p2 { font-size: 13px; }
  .bottle-label .p3 { font-size: 12px; margin-top: 2px; color: var(--green-dark); }
  .bottle-label .leaf-icon { width: 34px; height: 34px; margin-top: 22px; }
  .bottle-label .claims { padding-bottom: 10px; }
  .bottle-label .c1 { font-size: 15px; margin-bottom: 6px; }
  .bottle-label .c2, .bottle-label .c3 { font-size: 11px; }
  .bottle-label .volume-band { font-size: 13px; padding: 6px 0; margin-bottom: 12px; }
</style>
</head>
<body>
  <section class="carton" aria-label="Carton">
    <div class="carton-side">
      <div class="side-mark"><span class="leaf-icon" role="img" aria-label="Hemp leaf icon" style="width:34px;height:34px;background:var(--green-mid);opacity:.5"></span></div>
      <p class="side-copy">100% Colorado grown organic hemp. No psychoactive. No THC. High concentration of natural cannabinoids.</p>
      <div class="side-band">
        <div class="s1">Premium</div>
        <div class="s2">Full-Spectrum</div>
        <div class="s3">2000mg</div>
      </div>
      <p class="side-copy">Active Ingredients:<br>Marbleleaf Hemp 2000 mg<br><br>*Daily Value (DV) not established.</p>
      <div class="side-foot">1 fl oz (30ml)</div>
    </div>
    <div class="carton-front">
      <div class="brand-tile"><span class="dot"></span>Marbleleaf Hemp</div>
      <h1 class="title">Marbleleaf<br>Hemp</h1>
      <div class="strength-band">
        <div class="p1">Premium</div>
        <div class="p2">Full-Spectrum</div>
        <div class="p3">2000mg</div>
      </div>
      <div class="leaf-icon" role="img" aria-label="White hemp leaf icon"></div>
      <div class="claims">
        <div class="c1">Zero THC</div>
        <div class="c2">DIETARY SUPPLEMENT</div>
        <div class="c3">Natural Peppermint Flavor</div>
      </div>
      <div class="volume-band">1 fl oz (30ml)</div>
    </div>
  </section>

  <section class="bottle-label" aria-label="Bottle label">
    <div class="brand-tile"><span class="dot"></span>Marbleleaf Hemp</div>
    <h2 class="title">Marbleleaf<br>Hemp</h2>
    <div class="strength-band">
      <div class="p1">Premium</div>
      <div class="p2">Full-Spectrum</div>
      <div class="p3">2000mg</div>
    </div>
    <div class="leaf-icon" role="img" aria-label="White hemp leaf icon"></div>
    <div class="claims">
      <div class="c1">Zero THC</div>
      <div class="c2">DIETARY SUPPLEMENT</div>
      <div class="c3">Natural Peppermint Flavor</div>
    </div>
    <div class="volume-band">1 fl oz (30ml)</div>
  </section>
</body>
</html>
```